New business logo / Business Card Design

My company provides Interim Management and consultancy, for Facilities Services. Covers any aspect of facilities management, including M&E, helpdesk, asset management, supplier relationships, catering, cleaning etc. Company provides innovative solutions to exceed client needs, drawing on years of experience. Initial thoughts on logo are attached below. Fits with RAG status on projects, red, amber and green, with logo design colours around moving services from amber to green.

Target Market(s)

Facilities Management clients and service providers

Industry/Entity Type

Business

Contact Information for Business Card

Company Name = k7Rventures Ltd My name on card = Derek Whitcombe, Director Mobile = 07516309842 Email = Derek@k7rventuresltd.co.uk Twitter = @k7Rventures Ltd

Font styles to use
Sans Serif

Colors
f37122
00a990

Requirements
Must have
• Logo to be evident, with some background image in reference to Facilities Management

```html
<!DOCTYPE html>
<html lang="en">
<head>
<meta charset="utf-8">
<title>k7Rventures Ltd — Business Card</title>
<link rel="stylesheet" href="https://fonts.googleapis.com/css2?family=Arimo:wght@400;700&display=swap">
<style>
  :root {
    --bg: #3a3a3c;
    --card: #ffffff;
    --card-shade: #ececec;
    --ink: #1a1a1a;
    --ink-soft: #4a4a4a;
    --grey: #6b6b6b;
    --black-band: #050505;
    --amber: #f26a1b;
    --green: #2f8f2f;
  }
  * { box-sizing: border-box; margin: 0; padding: 0; }
  html, body {
    width: 1200px; height: 950px; overflow: hidden;
    background: var(--bg);
    font-family: "Arimo", Arial, sans-serif;
  }
  .stage { position: relative; width: 1200px; height: 950px; }

  .card {
    position: absolute;
    left: 260px;
    width: 680px; height: 390px;
    background: linear-gradient(160deg, var(--card) 55%, var(--card-shade) 100%);
    overflow: hidden;
    box-shadow: 0 10px 28px rgba(0,0,0,.45);
  }
  .card--back { top: 50px; }
  .card--front { top: 510px; }

  /* back */
  .back-brand {
    position: absolute; left: 0; right: 0; top: 130px;
    text-align: center;
    font-weight: 700; font-size: 96px; letter-spacing: 2px;
    color: var(--green);
  }
  .back-web {
    position: absolute; left: 0; right: 0; top: 260px;
    text-align: center;
    font-size: 20px; letter-spacing: 6px;
    color: var(--grey);
  }

  /* front */
  .front-band { position: absolute; inset: 0; width: 680px; height: 390px; }
  .holder { position: absolute; left: 40px; top: 34px; }
  .holder-name { font-size: 22px; font-weight: 700; color: var(--amber); }
  .holder-role { font-size: 14px; color: var(--green); margin-top: 4px; }

  .contacts {
    position: absolute; right: 36px; top: 206px;
    list-style: none; text-align: right;
    font-size: 18px; color: var(--ink-soft); line-height: 25px;
  }
  .contacts li { display: flex; justify-content: flex-end; align-items: center; gap: 10px; }
  .contacts svg { width: 16px; height: 16px; flex: none; }

  .front-brand {
    position: absolute; right: 36px; bottom: 30px;
    font-size: 42px; font-weight: 700; color: var(--ink);
    display: flex; align-items: center; gap: 12px;
  }
  .brand-dot { width: 16px; height: 16px; border-radius: 50%; background: var(--amber); }
</style>
</head>
<body>
<main class="stage">

  <section class="card card--back" aria-label="Card back">
    <div class="back-brand">k7R</div>
    <div class="back-web">k7rventuresltd.co.uk</div>
  </section>

  <section class="card card--front" aria-label="Card front">
    <svg class="front-band" viewBox="0 0 680 390" aria-hidden="true">
      <polygon points="0,0 680,0 680,70 0,170" fill="var(--black-band)"/>
      <polygon points="0,170 230,136.2 230,142.2 0,176" fill="var(--amber)"/>
      <polygon points="238,135 455,103.1 455,109.1 238,141" fill="var(--black-band)"/>
      <polygon points="463,101.9 680,70 680,76 463,107.9" fill="var(--green)"/>
    </svg>

    <div class="holder">
      <div class="holder-name">Derek Whitcombe</div>
      <div class="holder-role">Director</div>
    </div>

    <ul class="contacts">
      <li>07516309842
        <svg viewBox="0 0 16 16"><rect x="4" y="1" width="8" height="14" rx="1.5" fill="none" stroke="var(--amber)" stroke-width="2"/></svg>
      </li>
      <li>Derek@k7rventuresltd.co.uk
        <svg viewBox="0 0 16 16"><rect x="1" y="3" width="14" height="10" fill="var(--amber)"/><polyline points="1,3 8,9 15,3" fill="none" stroke="#fff" stroke-width="1.4"/></svg>
      </li>
      <li>k7rventuresltd.co.uk
        <svg viewBox="0 0 16 16"><circle cx="8" cy="8" r="7" fill="none" stroke="var(--amber)" stroke-width="2"/><line x1="1" y1="8" x2="15" y2="8" stroke="var(--amber)" stroke-width="1.5"/></svg>
      </li>
      <li>@k7Rventures Ltd
        <svg viewBox="0 0 16 16"><circle cx="8" cy="8" r="7" fill="var(--amber)"/></svg>
      </li>
    </ul>

    <div class="front-brand"><span class="brand-dot"></span>k7Rventures Ltd</div>
  </section>

</main>
</body>
</html>
```